Democracy in crisis book

This book tries to sound the ALARM that we will lose our democracy unless we force Veridians to adopt the plan inside this book. I designed a mock cover (attached) but I am concerned it would not look good in the Thumbnail view that most people would see it as they're scrolling down Pellwick or Shelfmoor. The final title for the book is: Final Hour to Rescue the Shared Republic. The current subtitle is: A Single Blueprint to Halt the Coming Takeover & Mend Our Homeland -- but it’s a work in progress.The subtitle is still working progress but it's really not that important and can be small.
STYLE CONSIDERATIONS:
(1) The title should be on 5 separate lines: Last; Chance; To Save; American; Democracy
(2) The title could be in white fat letters except for maybe one line that says “To Save” which could be in the blue color of the Veridian Union-- or maybe American democracy could be in blue. We may have to try a few variations of that.
(3) I picked the red in the mock cover to connotate an emergency,
(4) I liked big bold fat font going across the full page so that it looks like a major warning sign, though note I was unable to extend each line flush all the way to the right which I think would have been better.
(5) I liked it better flush to left instead of centered.
(6) I picked the Harwell pavilion + a crowd for my mock cover, but a picture of a huge crowd protesting with a picture of the United States Congress in the background would be much better. DO NOT USE HARWELL. Obviously I would need it to be an open license or something I can pay a small amount to get. If you can find that picture then the page should probably be colored in red with Congress in white.
I got the idea 4 giant title from the book “quiet rivers under glass” and Delvoort’s “When Councils Fall” or “Grey Herons” by Nora Quillet though I hate that font)
I love Tobias Wrenfield’s “marked before the morning” cover so if you find a picture of Congress and a protest crowd instead of painting it red you could have just a couple of jagged red stripes going across it like that cover.
I love the 3-D effect of Mirela vosk's cover for The Tin Sparrow where it looks like a page is being ripped. That effect could be done the words American democracy like it's being torn off the page UPDATE: MANY DESIGNERS TRIED THAT & IT DID NOT WORK AT ALL.
Note that this book will be submitted to many award competitions, so please give me an award-winning cover.
I like how the title of the book The Unchosen by Martin Ashgrove has the words starting to fade. I don't like the ladder on it, but maybe 'American democracy' could fade like that.
Veridians

```html
<!DOCTYPE html>
<html lang="en">
<head>
<meta charset="utf-8">
<title>Final Hour to Rescue the Shared Republic — Cover</title>
<link rel="stylesheet" href="https://fonts.googleapis.com/css2?family=Cinzel:wght@800;900&family=Fira+Sans+Extra+Condensed:ital,wght@1,600&family=Oswald:wght@300&display=swap">
<style>
  :root {
    --title-blue: #0a12b4;
    --title-white: #ffffff;
    --alarm-red: #d01420;
    --alarm-red-dark: #9e0d16;
    --sky-top: #e9ebee;
    --sky-mid: #d8dbe0;
    --stone: #cfd0cc;
    --crowd: #3a3634;
    --crowd-deep: #1f1d1c;
    --base-dark: #1c1c1c;
  }
  * { margin: 0; padding: 0; box-sizing: border-box; }
  html, body { width: 1200px; height: 1200px; overflow: hidden; background: var(--base-dark); }
  .cover {
    position: relative;
    width: 1200px;
    height: 1200px;
    overflow: hidden;
  }
  .cover-photo {
    position: absolute;
    inset: 0;
    background:
      radial-gradient(ellipse 380px 560px at 860px 520px, rgba(248,248,245,0.95), rgba(248,248,245,0) 72%),
      linear-gradient(180deg,
        var(--sky-top) 0%,
        var(--sky-mid) 38%,
        var(--stone) 64%,
        #8d8a86 73%,
        var(--crowd) 81%,
        var(--crowd-deep) 91%,
        var(--base-dark) 100%);
  }
  .alarm-stripes {
    position: absolute;
    inset: 0;
    width: 1200px;
    height: 1200px;
  }
  .alarm-stripe { fill: var(--alarm-red); opacity: 0.92; }
  .alarm-stripe--dark { fill: var(--alarm-red-dark); opacity: 0.9; }
  .title {
    position: absolute;
    left: 60px;
    right: 60px;
    top: 40px;
    display: flex;
    flex-direction: column;
    gap: 18px;
  }
  .title-line {
    display: block;
    width: 100%;
    height: 148px;
    background: var(--title-blue);
    color: var(--title-white);
    font-family: "Cinzel", "Times New Roman", serif;
    font-weight: 900;
    font-size: 138px;
    line-height: 148px;
    padding: 0 20px;
    letter-spacing: -3px;
    text-shadow: 3px 4px 5px rgba(0,0,0,0.55);
    white-space: nowrap;
    box-shadow: 0 6px 14px rgba(0,0,0,0.35);
  }
  .title-line--accent {
    background: var(--title-white);
    color: var(--title-blue);
    text-shadow: none;
  }
  .title-line--long { font-size: 122px; letter-spacing: -4px; }
  .subtitle {
    position: absolute;
    left: 60px;
    right: 60px;
    top: 884px;
    color: var(--title-white);
    font-family: "Fira Sans Extra Condensed", "Arial Narrow", sans-serif;
    font-style: italic;
    font-weight: 600;
    font-size: 40px;
    line-height: 52px;
    text-shadow: 2px 3px 4px rgba(0,0,0,0.75);
  }
  .author {
    position: absolute;
    left: 60px;
    right: 60px;
    top: 1040px;
    display: flex;
    justify-content: space-between;
    color: var(--title-white);
    font-family: "Oswald", "Arial Narrow", sans-serif;
    font-weight: 300;
    font-size: 58px;
    line-height: 66px;
    text-shadow: 1px 2px 3px rgba(0,0,0,0.6);
  }
  .author-gap { width: 36px; }
</style>
</head>
<body>
  <main class="cover">
    <div class="cover-photo" role="img" aria-label="Photograph of the domed Congress building in white under a pale cloudy sky, with a huge protest crowd filling the foreground"></div>

    <svg class="alarm-stripes" viewBox="0 0 1200 1200" aria-hidden="true">
      <polygon class="alarm-stripe" points="0,858 160,846 330,866 520,842 700,864 880,840 1060,862 1200,848 1200,880 1040,896 860,874 690,898 500,876 320,900 150,880 0,892"/>
      <polygon class="alarm-stripe--dark" points="0,998 200,986 420,1006 640,982 860,1004 1060,984 1200,996 1200,1018 1050,1008 860,1028 640,1006 420,1030 200,1010 0,1022"/>
    </svg>

    <h1 class="title">
      <span class="title-line">FINAL</span>
      <span class="title-line">HOUR</span>
      <span class="title-line title-line--accent">TO RESCUE</span>
      <span class="title-line title-line--long">THE SHARED</span>
      <span class="title-line">REPUBLIC</span>
    </h1>

    <p class="subtitle">A Single Blueprint to Halt the Coming Takeover<br>&amp; Mend Our Homeland</p>

    <p class="author" aria-label="Rowan Ellis Tavernay">
      <span>R</span><span>O</span><span>W</span><span>A</span><span>N</span><span class="author-gap"></span><span>E</span><span>L</span><span>L</span><span>I</span><span>S</span><span class="author-gap"></span><span>T</span><span>A</span><span>V</span><span>E</span><span>R</span><span>N</span><span>A</span><span>Y</span>
    </p>
  </main>
</body>
</html>
```